Property lawyer needs a website for new law firm Sydney

WHO AM I ?
I am a real estate development lawyer based in suburban Sydney Australia with over 14 years experience and have recently started my own law firm "Tallowbrook Legal". The firm is just me (a female) at this stage. I need a website designed that is capable of being edited by me frequently (hoping this is easily done?!) and can be published with the domain name I own - www.tallowbrooklegal.com.au.
My areas of practice are:
* Property development (strata & community titling, due diligence, easements, by-laws and management statements, structuring etc)
* Conveyancing (sale and purchase of residential, commercial and retail property)
* General property law (caveats, transfers, related party transactions, easements, leases, powers of attorney etc).
WEBSITE REQUIREMENTS
I would like a website which conveys professionalism, has a fresh modern corporate look and is easy to navigate. The website will mostly be accessed by potential clients looking for information about me, my areas of practice and how to get in contact with me. My potential clients are corporate developers and individuals who are buying and selling property.
My logo for Tallowbrook Legal (see attached) is simple, clean and professional looking. I would like the website to work with the logo without being too dark.
I haven't written all of the content yet, so please use filler text for everything and structure the menus as described above. The site will need to be capable of being updated and edited by me.
Other than that I will leave the design up to you.
Thanks and happy designing!
Target Market(s)
Professional developers and individuals buying and selling real estate
Industry/Entity Type
Real Estate
Coding
Coded - Design and coding required
Number of Pages Required
4 page
Requirements
Must have
- I would like a website which conveys professionalism, has a fresh modern corporate look and is easy to navigate. The website will mostly be accessed by potential clients looking for information about me, my areas of practice and how to get in contact with me. My potential clients are corporate developers and individuals who are buying and selling property.
- Please use my logo for Tallowbrook Legal. I would like the website to work with the logo - the colours are a dark blue (C 100% M 50% B 50%) and grey (C10% B 40%). I don't want the website to be too dark though.
- I am thinking 4 pages. I would like links across the top of the page for "Practice Areas", "About us" and "Contact us" - these should lead to separate landing pages with the content to be inserted later.
- The contact page should contain space for a potential client to send an email enquiry to the following email address "enquiries@tallowbrooklegal.com.au". My contact details are set out in the attached letterhead (see attached).
- I would also like the home page to set out what my three Practice Areas are - Property Development; Conveyancing; General Property Law. Each area should have some filler text under it which will be completed later and a link to be able to take me to the "Practice Areas" page where more detail on each will be provided.
- Please select images that are relevant to my practice as a property lawyer. The photos you use will be the ones which I use so please choose wisely.
- I will need a link on the bottom of the home page showing that I am a member of "The Counsel Guild of NSW" (see attached logo).
- The bottom of each page should also include the following statement "Tallowbrook Legal is a business name of Tallowbrook Legal Pty Limited ACN 482 517 306, an incorporated legal practice regulated by the Legal Profession Act 2004. Liability limited by a scheme approved under the Professional Standards Legislation."
Nice to have
- Have attached an image of me (not the best) but at least its me. Consider whether to use on "About us" page
Should not have
- No images of gavels, scales of justice or law books.
- Images not to be too masculine
- Website not to be too dark

```html
<!DOCTYPE html>
<html lang="en">
<head>
<meta charset="utf-8">
<title>About – Tallowbrook Legal</title>
<link rel="stylesheet" href="https://fonts.googleapis.com/css2?family=Noticia+Text:wght@400;700&family=Arimo:ital,wght@0,400;0,700;1,700&display=swap">
<style>
  :root {
    --paper: #ececeb;
    --brand-blue: #1f4f86;
    --nav-grey: #6b6b6b;
    --pill-navy: #28307c;
    --pill-edge: #151a55;
    --ink: #111111;
    --link-blue: #1e63ad;
    --rule: #d2d2d2;
    --band-top: #8799f2;
    --band-bottom: #6473da;
    --band-edge: #3c4bb0;
    --tab-navy: #2b3388;
    --panel: #ffffff;
    --fine-grey: #a4a4a4;
    --photo-light: #d9c2b2;
    --photo-dark: #2a2424;
  }
  * { margin: 0; padding: 0; box-sizing: border-box; }
  html, body { width: 1200px; height: 906px; overflow: hidden; }
  body {
    background: radial-gradient(ellipse at 40% 10%, #f1f1f0 0%, var(--paper) 60%, #e6e6e5 100%);
    font-family: "Noticia Text", Georgia, serif;
    color: var(--ink);
    position: relative;
    border-top: 1px solid #b9cde0;
  }
  .brand {
    position: absolute;
    font-family: "Noticia Text", Georgia, serif;
    font-weight: 700;
    color: var(--brand-blue);
    letter-spacing: -0.3px;
    white-space: nowrap;
  }
  .brand--header { left: 181px; top: 46px; font-size: 24px; }
  .brand--footer { left: 207px; top: 622px; font-size: 19px; }

  .main-nav { position: absolute; top: 47px; left: 0; width: 1200px; height: 27px; }
  .main-nav a {
    position: absolute; top: 0; height: 27px; line-height: 27px;
    font-weight: 700; font-size: 14px; color: var(--nav-grey); text-decoration: none;
  }
  .main-nav .nav-home { left: 656px; }
  .main-nav .nav-about {
    left: 726px; width: 103px; text-align: center; color: #fff;
    background: linear-gradient(#3a43a0, var(--pill-navy));
    border: 1px solid var(--pill-edge); border-radius: 8px;
  }
  .main-nav .nav-contact { left: 857px; }
  .main-nav .nav-areas { left: 950px; }

  .intro { position: absolute; left: 179px; top: 192px; font-size: 12px; }
  .intro-heading {
    position: absolute; left: 179px; top: 230px;
    font-family: "Arimo", Arial, Helvetica, sans-serif; font-style: italic; font-weight: 700;
    font-size: 25px; letter-spacing: 0.5px; white-space: nowrap;
  }
  .detail-list { position: absolute; left: 179px; top: 280px; list-style: none; }
  .detail-list li { height: 40px; font-size: 12px; font-weight: 700; letter-spacing: 0.3px; white-space: nowrap; }
  .detail-list a { color: var(--link-blue); text-decoration: none; }

  .portrait {
    position: absolute; left: 593px; top: 129px; width: 277px; height: 248px;
    background: linear-gradient(180deg, #f7f7f7 0%, var(--photo-light) 35%, #8a6f68 70%, var(--photo-dark) 100%);
  }

  .divider { position: absolute; left: 175px; top: 567px; width: 870px; height: 1px; background: var(--rule); }

  .site-footer { position: absolute; left: 179px; top: 602px; width: 861px; }
  .footer-band {
    position: absolute; left: 0; top: 0; width: 861px; height: 59px;
    background: linear-gradient(var(--band-top), var(--band-bottom));
    border: 1px solid var(--band-edge); border-radius: 4px;
    box-shadow: inset 0 1px 0 rgba(255,255,255,0.5);
  }
  .footer-tab { position: absolute; top: 58px; width: 18px; height: 11px; background: var(--tab-navy); }
  .footer-tab--left { left: 0; border-bottom-left-radius: 10px; }
  .footer-tab--right { right: 0; border-bottom-right-radius: 10px; }
  .footer-panel {
    position: absolute; left: 18px; top: 59px; width: 826px; height: 56px;
    background: var(--panel); box-shadow: 0 2px 3px rgba(0,0,0,0.12);
  }
  .footer-nav {
    position: absolute; left: 0; top: 29px; width: 826px; text-align: center;
    font-family: "Arimo", Arial, sans-serif; font-size: 9px; color: var(--fine-grey);
  }
  .footer-nav a { color: var(--fine-grey); text-decoration: none; margin: 0 6px; }
  .social-link { position: absolute; top: 20px; height: 23px; background: #141a3c; }
  .social-link--one { left: 712px; width: 22px; }
  .social-link--two { left: 755px; width: 23px; border-radius: 50%; }
  .social-link--three { left: 805px; width: 23px; }
  .copyright {
    position: absolute; left: 0; top: 734px; width: 1200px; text-align: center;
    font-family: "Arimo", Arial, sans-serif; font-size: 9px; color: var(--fine-grey);
  }
  .disclaimer {
    position: absolute; left: 250px; top: 756px; width: 700px; text-align: center;
    font-family: "Arimo", Arial, sans-serif; font-size: 9px; line-height: 13px; color: var(--fine-grey);
  }
</style>
</head>
<body>
  <header>
    <div class="brand brand--header">Tallowbrook Legal</div>
    <nav class="main-nav">
      <a class="nav-home" href="#">Home</a>
      <a class="nav-about" href="#">About</a>
      <a class="nav-contact" href="#">Contact</a>
      <a class="nav-areas" href="#">Prac. Areas</a>
    </nav>
  </header>

  <main>
    <p class="intro">Introduction here</p>
    <h1 class="intro-heading">About the Principal</h1>
    <ul class="detail-list">
      <li><a href="#">Practice overview</a></li>
      <li>14 years in property law practice</li>
      <li><a href="#">Areas of expertise</a></li>
      <li>Sydney-based solicitor</li>
      <li><a href="#">Qualifications</a></li>
      <li>Memberships</li>
    </ul>
    <div class="portrait" role="img" aria-label="Portrait photograph of the principal lawyer"></div>
  </main>

  <div class="divider"></div>

  <footer class="site-footer">
    <div class="footer-band"></div>
    <div class="footer-tab footer-tab--left"></div>
    <div class="footer-tab footer-tab--right"></div>
    <div class="footer-panel">
      <nav class="footer-nav">
        <a href="#">Home</a>|<a href="#">About</a>|<a href="#">Contact</a>|<a href="#">Prac. Areas</a>
      </nav>
    </div>
    <a class="social-link social-link--one" href="#" aria-label="Social profile"></a>
    <a class="social-link social-link--two" href="#" aria-label="Social profile"></a>
    <a class="social-link social-link--three" href="#" aria-label="Social profile"></a>
  </footer>
  <div class="brand brand--footer">Tallowbrook Legal</div>
  <p class="copyright">© Copyright © 2015 TALLOWBROOKLEGAL all rights reserved</p>
  <p class="disclaimer">Tallowbrook Legal is a business name of Tallowbrook Legal Pty Limited ACN 482 517 306, an incorporated legal practice regulated by the Legal Profession Act 2004. Liability limited by a scheme approved under the Professional Standards Legislation.</p>
</body>
</html>
```